Zenfro loop flyer

I want this flyer to look like the one I upload here called zenfro loop. I want the to change to words (headline):"A new category in pet hydration" to: Ny unik produkt i Kategori hund. Also remove Functional elektrodryck för hundar.
Also change:" Vi tar emot Återförsäljarpartners" to "Kontakta oss för mer information"
If you think or see improvments plase do so. Its for a launch of a newe product to retailers (so not to the consumer).

Target Market(s)

Retail, stores, hotels, restaurants

Industry/Entity Type

Energy water for dogs

Colors
0054AA
0677BA
7BADD7
CADEEF
E8F1F8

Requirements
Must have
• Think grimvolt, quorza pell, energy drinks but for dogs

```html
<!DOCTYPE html>
<html lang="sv">
<head>
<meta charset="utf-8">
<title>Zenfro loop – återförsäljarflyer</title>
<link href="https://fonts.googleapis.com/css2?family=Bebas+Neue&family=Poppins:wght@400;500;600;700&display=swap" rel="stylesheet">
<style>
  :root {
    --navy: #0b0f70;
    --gold: #b99a55;
    --red: #8c1a20;
    --paper: #f4f5f6;
    --panel-grey: #dfe2e8;
    --white: #ffffff;
    --text-dark: #0b0f70;
  }
  * { box-sizing: border-box; margin: 0; padding: 0; }
  html, body { width: 849px; height: 1200px; overflow: hidden; }
  body {
    position: relative;
    font-family: "Poppins", sans-serif;
    color: var(--text-dark);
    background: linear-gradient(180deg, #f8f8f9 0%, #eef0f2 60%, #f3f4f5 100%);
  }
  .abs { position: absolute; }

  /* Header */
  .brand { left: 63px; top: 100px; display: flex; align-items: center; gap: 10px; }
  .brand-dot { width: 26px; height: 26px; border-radius: 50%; background: #111; }
  .brand-name { font-family: "Poppins", sans-serif; font-weight: 700; font-size: 30px; color: #111; line-height: 1; }
  .header-divider { left: 287px; top: 94px; width: 3px; height: 57px; background: #111; }
  .tagline { left: 318px; top: 98px; font-size: 16px; font-weight: 500; letter-spacing: 2px; line-height: 25px; color: #111; }

  .ribbon { left: 651px; top: 0; width: 134px; height: 199px; }
  .ribbon-text { left: 651px; top: 74px; width: 134px; text-align: center; color: var(--gold); font-size: 16px; font-weight: 500; line-height: 22px; }
  .flag { left: 697px; top: 127px; }

  /* Headline */
  .headline { left: 62px; top: 222px; font-family: "Bebas Neue", sans-serif; font-size: 86px; line-height: 76px; color: var(--navy); }
  .headline .accent { color: var(--gold); }

  /* Product photo */
  .product-photo {
    left: 305px; top: 195px; width: 290px; height: 770px;
    border-radius: 60px 60px 30px 30px;
    background: linear-gradient(90deg, #dfe6ee 0%, #f5f8fb 30%, #1d3fb8 45%, #0e1f92 70%, #e3e9f0 100%);
    opacity: 0.9;
  }

  /* Feature list */
  .intro { left: 554px; top: 256px; font-size: 12.5px; line-height: 22px; color: var(--navy); }
  .gold-rule { height: 2px; background: var(--gold); }
  .feature { left: 555px; display: flex; gap: 10px; }
  .feature-icon { width: 56px; height: 56px; border-radius: 50%; flex: none; display: flex; align-items: center; justify-content: center; }
  .feature h3 { font-size: 13px; font-weight: 700; line-height: 19px; color: var(--navy); margin-top: -2px; }
  .feature p { font-size: 10.5px; line-height: 17.5px; margin-top: 4px; color: var(--navy); }
  .feature-sep { left: 555px; width: 220px; height: 1px; background: #cfd2d8; }

  /* Retailer panel */
  .retail-panel { left: 0; top: 566px; width: 305px; height: 366px; background: var(--navy); border-radius: 0 26px 26px 0; color: var(--white); }
  .retail-title { position: absolute; left: 64px; top: 20px; font-size: 14.5px; font-weight: 600; line-height: 21px; }
  .retail-rule { position: absolute; left: 64px; top: 68px; width: 198px; }
  .reason { position: absolute; left: 64px; display: flex; gap: 8px; }
  .reason-icon { width: 48px; height: 48px; border-radius: 50%; background: var(--gold); flex: none; display: flex; align-items: center; justify-content: center; }
  .reason h4 { font-size: 10.5px; font-weight: 400; line-height: 13.5px; }
  .reason p { font-size: 9.3px; line-height: 14px; margin-top: 2px; }

  /* Category box */
  .category { left: 603px; top: 668px; width: 182px; height: 250px; background: var(--panel-grey); border-radius: 18px; }
  .category h3 { position: absolute; left: 18px; top: 28px; font-size: 12.5px; font-weight: 700; }
  .category .gold-rule { position: absolute; left: 18px; top: 53px; width: 40px; }
  .category p { position: absolute; left: 18px; top: 66px; font-size: 9.5px; line-height: 17px; width: 160px; }
  .category svg { position: absolute; left: 22px; top: 130px; }
  .category .demand { position: absolute; left: 18px; top: 196px; font-size: 11px; line-height: 16.5px; }

  /* Footer */
  .claim-band { left: 0; top: 980px; width: 849px; height: 220px; background: var(--navy); }
  .claim { left: 64px; top: 959px; width: 722px; height: 41px; border-radius: 20px; background: var(--gold); color: var(--navy); font-size: 14.5px; font-weight: 700; display: flex; align-items: center; justify-content: center; }
  .contact-title { left: 63px; top: 1048px; font-family: "Bebas Neue", sans-serif; font-size: 54px; line-height: 50px; color: var(--white); }
  .contact-sub { left: 64px; top: 1097px; font-size: 14px; color: var(--white); }
  .footer-divider { top: 1032px; width: 2px; height: 105px; background: var(--gold); }
  .contacts { left: 360px; top: 1038px; list-style: none; color: var(--white); font-size: 13px; }
  .contacts li { display: flex; align-items: center; gap: 12px; height: 34.5px; }
  .launch-label { left: 614px; top: 1030px; width: 172px; text-align: center; color: var(--white); font-size: 12px; }
  .launch-date { left: 614px; top: 1057px; width: 172px; height: 33px; background: var(--gold); color: var(--navy); font-weight: 700; font-size: 16px; display: flex; align-items: center; justify-content: center; }
  .launch-note { left: 627px; top: 1098px; color: var(--white); font-size: 12.5px; line-height: 20px; }
</style>
</head>
<body>

<header>
  <div class="abs brand"><span class="brand-dot"></span><span class="brand-name">zenfro loop</span></div>
  <div class="abs header-divider"></div>
  <p class="abs tagline">FUNCTIONAL HYDRATION<br>FÖR HUNDAR</p>

  <svg class="abs ribbon" viewBox="0 0 134 199"><polygon points="0,0 134,0 134,199 67,171 0,199" fill="var(--navy)"/></svg>
  <p class="abs ribbon-text">TILLVERKAD I<br>SVERIGE</p>
  <svg class="abs flag" width="42" height="26" viewBox="0 0 42 26"><rect width="42" height="26" fill="#0b5cd6"/><rect x="12" width="6" height="26" fill="#f8d20c"/><rect y="10" width="42" height="6" fill="#f8d20c"/></svg>
</header>

<h1 class="abs headline">NY UNIK<br>PRODUKT<br><span class="accent">I KATEGORI<br>HUND</span></h1>

<div class="abs product-photo" role="img" aria-label="Produktfoto: genomskinlig 500 ml-flaska med svart kork och blå etikett, stående i vattenstänk"></div>

<p class="abs intro">Utvecklad för alla hundar.<br>Inspirerad av human sportdryck.</p>
<div class="abs gold-rule" style="left:554px;top:313px;width:53px;"></div>

<div class="abs feature" style="top:342px;">
  <div class="feature-icon" style="background:var(--navy)">
    <svg width="28" height="28" viewBox="0 0 28 28" fill="none" stroke="#fff" stroke-width="1.5"><path d="M14 3 C9 10 6 14 6 18 a8 8 0 0 0 16 0 c0-4-3-8-8-15z"/><path d="M15 11 l-4 7 h4 l-2 5 5-8 h-4z"/></svg>
  </div>
  <div><h3>NATURLIGA<br>ELEKTROLYTER</h3><p>Återställer vätska<br>och stödjer balansen.</p></div>
</div>
<div class="abs feature-sep" style="top:426px;"></div>

<div class="abs feature" style="top:444px;">
  <div class="feature-icon" style="background:var(--red)">
    <svg width="28" height="28" viewBox="0 0 28 28" fill="none" stroke="#fff" stroke-width="1.5"><path d="M14 8 c-2 3-3 4-3 6 a3 3 0 0 0 6 0 c0-2-1-3-3-6z"/><path d="M8 5 c-1 2-2 3-2 4 a2 2 0 0 0 4 0 c0-1-1-2-2-4z"/><path d="M20 5 c-1 2-2 3-2 4 a2 2 0 0 0 4 0 c0-1-1-2-2-4z"/><ellipse cx="14" cy="21" rx="9" ry="3"/></svg>
  </div>
  <div><h3>STÖDJER HYDRERING<br>&amp; ÅTERHÄMTNING</h3><p>Hjälper till att upprätthålla<br>prestationsförmåga<br>och välmående.</p></div>
</div>
<div class="abs feature-sep" style="top:547px;"></div>

<div class="abs feature" style="top:563px;">
  <div class="feature-icon" style="background:var(--gold)">
    <svg width="36" height="20" viewBox="0 0 36 20" fill="none" stroke="#fff" stroke-width="1.5"><path d="M1 11 h9 l3-8 4 15 3-9 2 4 h5"/><path d="M29 13 h2 M33 13 h2"/></svg>
  </div>
  <div><h3>PERFEKT EFTER AKTIVITET,<br>VÄRME &amp; RESA</h3><p>För vardagens äventyr och<br>särskilda tillfällen.</p></div>
</div>

<section class="abs retail-panel">
  <h2 class="retail-title">VARFÖR ÅTERFÖRSÄLJARE<br>VÄLJER ZENFRO LOOP</h2>
  <div class="gold-rule retail-rule"></div>

  <div class="reason" style="top:85px;">
    <div class="reason-icon"><svg width="26" height="22" viewBox="0 0 26 22" fill="none" stroke="var(--navy)" stroke-width="2.2"><path d="M2 2 v18 h22"/><path d="M6 15 l6-6 4 3 7-7"/><path d="M18 5 h5 v5"/></svg></div>
    <div><h4>HÖG MARGINAL.<br>LITEN KONKURRENS</h4><p>Var först på en växande<br>kategori.</p></div>
  </div>
  <div class="reason" style="top:156px;">
    <div class="reason-icon"><svg width="26" height="24" viewBox="0 0 26 24" fill="none" stroke="var(--navy)" stroke-width="2.2"><path d="M2 3 h4 l3 12 h12 l3-9 H8"/><circle cx="10" cy="20" r="1.8"/><circle cx="19" cy="20" r="1.8"/></svg></div>
    <div><h4>SNABBT VÄXANDE SEGMENT<br>INOM HUNDHÄLSA</h4><p>Stark och ökande efterfrågan<br>från medvetna hundägare.</p></div>
  </div>
  <div class="reason" style="top:226px;">
    <div class="reason-icon"><svg width="26" height="24" viewBox="0 0 26 24" fill="none" stroke="var(--navy)" stroke-width="2.2"><path d="M13 21 C4 14 2 10 2 7 a5 5 0 0 1 11-1 a5 5 0 0 1 11 1 c0 3-2 7-11 14z"/></svg></div>
    <div><h4>STOR IMPULSKÖPSPOTENTIAL</h4><p>Perfekt att placera vid vatten<br>och snacks.</p></div>
  </div>
  <div class="reason" style="top:296px;">
    <div class="reason-icon"><svg width="26" height="26" viewBox="0 0 26 26" fill="none" stroke="var(--navy)" stroke-width="2.2"><path d="M14 3 h9 v9 L12 23 3 14z"/><circle cx="18" cy="8" r="1.6"/></svg></div>
    <div><h4>PREMIUMPOSITIONERING<br>= HÖGRE KUNDVÄRDE</h4><p>Ger mer värde i varje besök.</p></div>
  </div>
</section>

<section class="abs category">
  <h3>KATEGORIMÖJLIGHET</h3>
  <div class="gold-rule"></div>
  <p>Hudhydrering för hundar är ett outnyttjat segment med stor tillväxtpotential.</p>
  <svg width="56" height="52" viewBox="0 0 56 52" fill="var(--navy)"><rect x="0" y="42" width="8" height="8"/><rect x="12" y="36" width="8" height="14"/><rect x="24" y="28" width="8" height="22"/><rect x="38" y="18" width="10" height="32"/><path d="M0 36 Q22 30 44 8" fill="none" stroke="var(--navy)" stroke-width="4"/><polygon points="38,4 52,0 50,14"/></svg>
  <p class="demand">VÄXANDE EFTERFRÅGAN<br>I HELA EUROPA</p>
</section>

<footer>
  <div class="abs claim-band"></div>
  <div class="abs claim">RENA INGREDIENSER. VERKLIGA FÖRDELAR. HUNDAR KÄNNER SKILLNADEN.</div>

  <h2 class="abs contact-title">KONTAKTA OSS</h2>
  <p class="abs contact-sub">FÖR MER INFORMATION</p>
  <div class="abs footer-divider" style="left:318px;"></div>

  <ul class="abs contacts">
    <li><svg width="14" height="18" viewBox="0 0 14 18" fill="none" stroke="#fff" stroke-width="1.6"><rect x="2" y="1" width="10" height="16" rx="1.5"/><path d="M6 14 h2"/></svg>+46 70 555 01 23</li>
    <li><svg width="16" height="12" viewBox="0 0 16 12"><rect width="16" height="12" rx="1" fill="#fff"/><path d="M1 1 l7 6 7-6" fill="none" stroke="var(--navy)" stroke-width="1.4"/></svg>info@zenfroloop.com</li>
    <li><svg width="16" height="16" viewBox="0 0 16 16" fill="none" stroke="#fff" stroke-width="1.4"><circle cx="8" cy="8" r="7"/><ellipse cx="8" cy="8" rx="3" ry="7"/><path d="M1 8 h14 M2 4.5 h12 M2 11.5 h12"/></svg>zenfroloop.com</li>
  </ul>

  <div class="abs footer-divider" style="left:561px;"></div>
  <p class="abs launch-label">— BEGRÄNSAD LANSERING —</p>
  <div class="abs launch-date">SOMMAREN 2026</div>
  <p class="abs launch-note">Säkra din tilldelning<br>i tid och möt efterfrågan.</p>
</footer>

</body>
</html>
```